Solar energy proposal for homeowners

I am providing households with solar energy proposals, and I need a high-quality brochure that is packaged cleverly to attract the homeowner's attention. Take a look at the one page solar brochure that I have included to get an idea of text and content.

Target Market(s)

Residential Homeowners

Industry/Entity Type

Solar

Requirements
Must have
• High quality document

```html
<!DOCTYPE html>
<html lang="en">
<head>
<meta charset="utf-8">
<title>Heliovale Energy – Solar for $0 Down</title>
<link href="https://fonts.googleapis.com/css2?family=Bebas+Neue&family=Arimo:wght@400;700&display=swap" rel="stylesheet">
<style>
  :root {
    --navy: #16329a;
    --navy-deep: #0f2780;
    --panel-blue: #2f5a93;
    --sky: #bfe3f5;
    --lime: #8ee33a;
    --mint: #7fe0a8;
    --teal: #1fc7b4;
    --white: #ffffff;
    --bar: #3b68a6;
  }
  * { margin: 0; padding: 0; box-sizing: border-box; }
  html, body { width: 849px; height: 1200px; overflow: hidden; background: #ffffff; }
  .brochure {
    position: relative;
    width: 849px;
    height: 1200px;
    overflow: hidden;
    font-family: "Arimo", Arial, sans-serif;
    color: var(--white);
    background: var(--navy);
  }
  .backdrop { position: absolute; inset: 0; }

  .brand-name {
    position: absolute;
    left: 40px;
    top: 78px;
    font-family: "Arimo", Arial, sans-serif;
    font-weight: 700;
    font-size: 50px;
    line-height: 1;
    color: var(--mint);
    letter-spacing: 0.5px;
  }

  .headline {
    position: absolute;
    right: 509px;
    top: 548px;
    font-family: "Bebas Neue", "Arial Narrow", sans-serif;
    font-size: 76px;
    line-height: 61px;
    text-align: right;
    white-space: nowrap;
  }
  .tagline {
    position: absolute;
    left: 88px;
    top: 802px;
    font-weight: 700;
    font-size: 17.5px;
    line-height: 21px;
    color: var(--lime);
  }
  .divider {
    position: absolute;
    left: 353px;
    top: 467px;
    width: 3px;
    height: 390px;
    background: var(--white);
  }

  .info { position: absolute; left: 386px; width: 424px; }
  .info h2 { font-weight: 700; font-size: 31px; line-height: 1; }
  .about { top: 507px; }
  .about p {
    margin-top: 12px;
    font-weight: 700;
    font-size: 14.6px;
    line-height: 19px;
    text-align: justify;
    letter-spacing: 0.2px;
  }
  .accent { color: var(--lime); }
  .why { top: 690px; }
  .why ul { list-style: none; margin-top: 8px; }
  .why li { font-weight: 700; font-size: 15.5px; line-height: 19.2px; }

  .services-title {
    position: absolute;
    left: 0; right: 0;
    top: 874px;
    text-align: center;
    font-weight: 700;
    font-size: 31px;
  }
  .service { position: absolute; width: 292px; }
  .service .icon { position: absolute; left: -63px; top: -3px; width: 50px; height: 50px; }
  .service h3 { font-weight: 700; font-size: 19.5px; line-height: 22px; color: var(--mint); }
  .service p { margin-top: 2px; font-size: 15.5px; line-height: 19px; text-align: justify; }
  .svc-affordable { left: 103px; top: 933px; }
  .svc-install { left: 511px; top: 933px; }
  .svc-install p { letter-spacing: 1.4px; }
  .svc-local { left: 103px; top: 1044px; }
  .svc-eco { left: 511px; top: 1044px; }

  .contact {
    position: absolute;
    top: 1160px;
    height: 34px;
    background: var(--bar);
    display: flex;
    align-items: center;
    font-size: 16.5px;
  }
  .contact .glyph {
    width: 33px; height: 34px;
    background: var(--white);
    margin-left: 7px;
    display: flex; align-items: center; justify-content: center;
  }
  .contact span { margin-left: 20px; white-space: nowrap; }
  .contact-phone { left: 9px; width: 264px; }
  .contact-address { left: 292px; width: 264px; }
  .contact-web { left: 575px; width: 250px; }
  .contact-web span { margin-left: 22px; }
</style>
</head>
<body>
<main class="brochure">
  <svg class="backdrop" width="849" height="1200" viewBox="0 0 849 1200">
    <defs>
      <linearGradient id="houseTone" x1="0" y1="0" x2="1" y2="1">
        <stop offset="0" stop-color="#9cc9e6"/>
        <stop offset="0.45" stop-color="#7a8faa"/>
        <stop offset="0.8" stop-color="#a48470"/>
        <stop offset="1" stop-color="#5f7a45"/>
      </linearGradient>
      <linearGradient id="arrayTone" x1="0" y1="0" x2="0.4" y2="1">
        <stop offset="0" stop-color="#1a3aa6"/>
        <stop offset="0.6" stop-color="#1c3d9e"/>
        <stop offset="1" stop-color="#3a64b8"/>
      </linearGradient>
      <linearGradient id="swoosh" x1="0" y1="0" x2="1" y2="0">
        <stop offset="0" stop-color="var(--teal)"/>
        <stop offset="1" stop-color="var(--lime)"/>
      </linearGradient>
    </defs>
    <rect role="img" aria-label="Photo of a brick house with solar panels on a tiled roof in sunshine" x="0" y="0" width="849" height="560" fill="url(#houseTone)"/>
    <path role="img" aria-label="Close-up photo of a solar panel surface" d="M0 0 H849 V14 C600 55 300 165 0 392 Z" fill="var(--panel-blue)"/>
    <path d="M849 14 C600 55 300 165 0 392" fill="none" stroke="url(#swoosh)" stroke-width="14"/>
    <path role="img" aria-label="Photo of rows of blue solar panels" d="M0 548 C200 468 450 420 849 476 V1200 H0 Z" fill="url(#arrayTone)"/>
    <path d="M0 540 C200 460 450 412 849 468" fill="none" stroke="url(#swoosh)" stroke-width="14"/>
  </svg>

  <div class="brand-name">Heliovale Energy</div>

  <h1 class="headline">SOLAR FOR $0<br>DOWN.<br>NO LIENS.<br>NOKIDDING.</h1>
  <p class="tagline">Power Your Future with<br>Heliovale Energy</p>

  <div class="divider"></div>

  <section class="info about">
    <h2>About Us</h2>
    <p>At <span class="accent">Heliovale Energy</span>, our mission is to make solar simple and accessible for everyone. No high-pressure sales just the information you need to make a smart choice. With our solar <span class="accent">rental program</span>, you can lower your monthly energy costs and <span class="accent">pay less</span> than your current electricity bill.</p>
  </section>

  <section class="info why">
    <h2>Why Choose Us?</h2>
    <ul>
      <li><span class="accent">No</span> financing</li>
      <li><span class="accent">No</span> liens</li>
      <li><span class="accent">No</span> down payment</li>
      <li><span class="accent">No</span> insurance costs</li>
      <li><span class="accent">No</span> long-term commitment</li>
      <li><span class="accent">No</span> maintenance costs</li>
    </ul>
  </section>

  <h2 class="services-title">Our Best Service</h2>

  <div class="service svc-affordable">
    <svg class="icon" viewBox="0 0 50 50"><circle cx="25" cy="25" r="24" fill="#3fae96" stroke="#fff" stroke-width="1.5"/><circle cx="25" cy="22" r="7" fill="none" stroke="#fff" stroke-width="1.6"/><path d="M22 30h6M22 33h6M25 8v4M13 12l3 3M37 12l-3 3M9 22h4M41 22h-4" stroke="#fff" stroke-width="1.6"/></svg>
    <h3>Affordable &amp; Transparent</h3>
    <p>Simple pricing, no hidden fees and fixed monthly rate lower than typical energy bills</p>
  </div>
  <div class="service svc-install">
    <svg class="icon" viewBox="0 0 50 50"><circle cx="25" cy="25" r="24" fill="#3fae96" stroke="#fff" stroke-width="1.5"/><circle cx="22" cy="27" r="8" fill="none" stroke="#fff" stroke-width="2" stroke-dasharray="3 2"/><circle cx="22" cy="27" r="3" fill="none" stroke="#fff" stroke-width="1.6"/><circle cx="32" cy="17" r="5" fill="none" stroke="#fff" stroke-width="1.6" stroke-dasharray="2 1.5"/></svg>
    <h3>Expert Installation</h3>
    <p>Certified professionals handle installation, maintenance, and repairs end to end.</p>
  </div>
  <div class="service svc-local">
    <svg class="icon" viewBox="0 0 50 50"><circle cx="25" cy="25" r="24" fill="#3fae96" stroke="#fff" stroke-width="1.5"/><circle cx="24" cy="26" r="11" fill="none" stroke="#fff" stroke-width="1.6"/><circle cx="24" cy="26" r="6" fill="none" stroke="#fff" stroke-width="1.6"/><circle cx="24" cy="26" r="2" fill="#fff"/><path d="M24 26l12-12M33 13h4v4" stroke="#fff" stroke-width="1.6" fill="none"/></svg>
    <h3>Local Expertise</h3>
    <p>Florida-based team that understands the needs of orlando and statewide home owners.</p>
  </div>
  <div class="service svc-eco">
    <svg class="icon" viewBox="0 0 50 50"><circle cx="25" cy="25" r="24" fill="#3fae96" stroke="#fff" stroke-width="1.5"/><path d="M15 35c0-12 8-19 20-20 0 12-8 20-20 20z" fill="none" stroke="#fff" stroke-width="1.6"/><path d="M15 35l14-14" stroke="#fff" stroke-width="1.6"/></svg>
    <h3>Eco-Friendly</h3>
    <p>Clean, renewable solar energy that helps reduce your carbon footprint.</p>
  </div>

  <div class="contact contact-phone">
    <div class="glyph"><svg width="20" height="20" viewBox="0 0 24 24"><path d="M5 3h4l2 5-2.5 1.5a11 11 0 0 0 6 6L16 13l5 2v4a2 2 0 0 1-2 2A16 16 0 0 1 3 5a2 2 0 0 1 2-2z" fill="none" stroke="#333" stroke-width="1.5"/></svg></div>
    <span>(407) 555-0148</span>
  </div>
  <div class="contact contact-address">
    <div class="glyph"><svg width="20" height="22" viewBox="0 0 20 22"><rect x="3" y="2" width="9" height="18" fill="none" stroke="#333" stroke-width="1.3"/><rect x="12" y="9" width="6" height="11" fill="none" stroke="#333" stroke-width="1.3"/><path d="M5 5h2M8 5h2M5 9h2M8 9h2M5 13h2M8 13h2M14 12h2M14 15h2" stroke="#333" stroke-width="1.2"/></svg></div>
    <span>123 Anywhere St., Any City</span>
  </div>
  <div class="contact contact-web">
    <div class="glyph"><svg width="22" height="22" viewBox="0 0 24 24"><circle cx="12" cy="12" r="10" fill="none" stroke="#333" stroke-width="1.5"/><ellipse cx="12" cy="12" rx="4.5" ry="10" fill="none" stroke="#333" stroke-width="1.3"/><path d="M2 12h20M4 7h16M4 17h16" stroke="#333" stroke-width="1.3"/></svg></div>
    <span>www.heliovaleenergy.com</span>
  </div>
</main>
</body>
</html>
```